Beacon Crest Service HVAC Card

Sale, Install, Maintenance Commercial Vent Hood, Ice Machine & Refrigeration
Air Conditioning Heating & Cooling

Industry/Entity Type

Air Conditioning

Contact Information for Business Card

Beacon Crest Service
2847 Marlowe Ave.
Cedar Bend Tx, 75501
Ph. (555) 482-7193 Tomas B. Villareal Owner
Ph. (555) 619-2084 Hugo Saldivar Tec.
E-mail. beaconcrest2847@mailbrook.example

```html
<!DOCTYPE html>
<html lang="en">
<head>
<meta charset="utf-8">
<title>Beacon Crest Service – Business Card</title>
<link rel="stylesheet" href="https://fonts.googleapis.com/css2?family=Caveat+Brush&family=Caladea:wght@400;700&display=swap">
<style>
  :root {
    --card-top: #ffffff;
    --card-light: #e6e6e7;
    --card-mid: #a9a9ab;
    --card-deep: #5a5a5c;
    --card-bottom: #1f1f20;
    --ink: #1a1a1a;
    --ink-light: #ffffff;
  }
  html, body {
    margin: 0;
    padding: 0;
    width: 1200px;
    height: 700px;
    overflow: hidden;
    background: var(--card-top);
  }
  .business-card {
    position: relative;
    width: 1200px;
    height: 700px;
    overflow: hidden;
    background: linear-gradient(to bottom,
      var(--card-top) 0%,
      var(--card-light) 30%,
      var(--card-mid) 58%,
      var(--card-deep) 80%,
      var(--card-bottom) 100%);
    font-family: "Caladea", "Cambria", serif;
    color: var(--ink);
  }
  .company-name {
    position: absolute;
    left: 46px;
    top: 56px;
    margin: 0;
    font-family: "Caveat Brush", cursive;
    font-weight: 400;
    font-size: 104px;
    line-height: 1;
    letter-spacing: 0.5px;
  }
  .company-address {
    position: absolute;
    left: 37px;
    top: 168px;
    margin: 0;
    font-style: normal;
    font-size: 47px;
    line-height: 63px;
  }
  .company-email {
    position: absolute;
    left: 30px;
    top: 300px;
    margin: 0;
    font-size: 32px;
  }
  .contact {
    position: absolute;
    color: var(--ink-light);
  }
  .contact--owner { left: 56px; top: 560px; }
  .contact--tech { left: 630px; top: 558px; }
  .contact-name {
    margin: 0;
    font-weight: 700;
    font-size: 42px;
    font-variant: small-caps;
    letter-spacing: 1px;
    line-height: 1;
    word-spacing: 8px;
  }
  .contact-role {
    font-weight: 400;
    font-variant: normal;
    font-size: 29px;
    letter-spacing: 0;
    word-spacing: 0;
  }
  .contact-phone {
    margin: 10px 0 0;
    font-size: 29px;
    line-height: 1;
  }
</style>
</head>
<body>
  <main class="business-card">
    <h1 class="company-name">Beacon Crest Service</h1>
    <address class="company-address">2847 Marlowe Ave.<br>Cedar Bend Tx, 75501</address>
    <p class="company-email">E-mail: beaconcrest2847@mailbrook.example</p>

    <section class="contact contact--owner">
      <p class="contact-name">Tomas B. Villareal<span class="contact-role">, Owner</span></p>
      <p class="contact-phone">Ph. (555) 482-7193</p>
    </section>

    <section class="contact contact--tech">
      <p class="contact-name">Hugo Saldivar<span class="contact-role">, Tec</span></p>
      <p class="contact-phone">Ph. (555) 619-2084</p>
    </section>
  </main>
</body>
</html>
```